Wordpress Design Project

WHO WE ARE:
Bright Path Web Growth is not just another SEO or PPC company. We work with our clients to help them grow their business and achieve their goals. Our commitment to doing what is best for the customer, is why we have grown so quickly. We believe our business is not about advertising BUT about connecting customers & growing our clients businesses. We see our product as helping people, not selling a product.

PROJECT OVERVIEW:
I need to create a wordpress website for my business, www.brightpathwebgrowth.com.au

I need a whole new site created showing all of my services. The services include:
NOTE: These are not the main focus of the home page.

Consulting & Strategy Planning
Search Engine Optimisation
Pay Per Click
Re-Marketing

Once I have selected the top home page design, I will need a product and blog page designed.

SITE DESIGN:
If I was to explain the kind of style I am looking for, it would be high-street, New York agency look, web 2.0. Clean, elegant, stylish, high quality and simple looking. Kind of like you would expect from an quince website.

Think of car advertising, the closest to the target market & look/feel Im looking for would be Ravenmotor, Korel, Tamar, Brandin, Zepra.

However, I am open to any design style.

DO NOT let this restrict your creativity BUT here are some websites I like the look of.

Home page:
http://www.layoutfoundry.example/demo/52816.html
https://www.vantorix.example/intl/en/halo/devices/
http://www.vantorix.example/intl/en/halo/devices/features-different.html
http://www.layoutfoundry.example/demo/47190.html
https://www.vantorix.example/intl/en/halo/browser/features.html

Product Page:
http://www.vantorix.example/intl/en/halo/devices/buynow.html#instore

NOTE: I just added a file called "I like this color scheme.png" you can play around with something like this as well.
Updates

Please do not use the content from my current website. That is for a PPC service, the new site is for an full service agency.

Also, the message/tagline is the feature or most prominent element of the website..... Not the services we offer, these are secondary.

Great designs so far everyone, but I think I'm looking a little simpler and less crowded.  Closer to the sample sites I sent.... keep em coming.

Also, I would prefer that the 4 services, do not visually over power the tag line.  The 4 services are not important to the home page.

Lets make this easy, since every design I receive is almost the same...

Make the design look something like these 2 websites.
https://www.vantorix.example/intl/en/halo/browser/features.html#simplicity

Target Market(s)

Business Owners and entreprenuers who are well established, typically in the 35-60 year old range and spend 100k-1m in advertising per year. They big brands that target these people are Ravenmotor, Korel, Tamar, Brandin, Zepra, this should give you the feel for what I am after.

Industry/Entity Type

Advertising

Requirements
Must have
• 1. Navigations: Home, Services, About Us, Blog, Contact Us

2. The main home page words should be.... "We Grow Your Business Online" and "Clear Aim, Clear Plan, Clear Team, Bright Path Web Growth" (should use logo for last one)
I would like to see this tagline somewhere in the site "We Don't Want to be the Biggest, Just the Best!"

3. Product page must have a contact form with (name, email, phone, website)
This form must show an offer of "Free Strategy Sessions, Double your website leads", I have included an image to show as an example for the lead form "lead form example.png", see attached.

Nice to have
• I would like to see 1 or 2 of these idea's in the design.

1. I have attached some logos for Bidlane & Metricove certifications + Web association logo you can use for design purposes.

2. You can put company logo's in the design and I can change them to my clients logos at a later date.

3. Testimonials

4. Since our business is about people, pictures of people like business owners, customers using technology such as an slate, or anything like that would be good. However, is not necessary. Some idea: http://www.peerlattice.example/advertising
Should not have
• There will be no video on the design.

```html
<!DOCTYPE html>
<html lang="en">
<head>
<meta charset="utf-8">
<title>Bright Path Web Growth</title>
<link rel="stylesheet" href="https://fonts.googleapis.com/css2?family=Arimo:wght@400;700&display=swap">
<style>
:root{
  --blue:#1c78d4;
  --blue-dark:#0e55a8;
  --ink:#222;
  --text:#444;
  --muted:#8a8a8a;
  --orange:#ee6a0c;
  --orange-light:#ff9630;
  --footer:#393939;
  --footer-line:#5a5a5a;
  --footer-text:#8d8d8d;
}
*{box-sizing:border-box;margin:0;padding:0}
html,body{width:916px;height:1200px;overflow:hidden;background:#fff}
body{position:relative;font-family:"Arimo",Arial,sans-serif;color:var(--text)}
.abs{position:absolute}

/* header */
.brand{left:26px;top:40px;display:flex;align-items:center;gap:10px}
.brand-dot{width:34px;height:34px;border-radius:50%;background:var(--blue)}
.brand-name{font-size:19px;font-weight:700;color:#333;letter-spacing:-.2px}
.nav{top:62px;left:494px;display:flex;gap:27px;font-size:12.6px;color:#444;list-style:none}
.nav li.active{color:var(--blue)}

/* hero */
.hero{left:0;top:106px;width:886px;height:329px;background:linear-gradient(90deg,#c9d6e4 0%,#e9eef3 40%,#f4f6f8 60%,#e3e8ee 100%)}
.hero-photo{position:absolute;left:440px;top:0;width:446px;height:329px;background:linear-gradient(180deg,#e9edf1 0%,#9fb1c6 55%,#2f4464 100%);opacity:.85}
.tagline{position:absolute;right:453px;top:112px;text-align:right;font-size:21px;line-height:27.5px;color:#333;letter-spacing:-.2px;text-transform:uppercase}
.tagline b{font-weight:400;color:#1a1a1a}
.tagline span{font-weight:400;color:#555}
.dots{position:absolute;left:48px;top:306px;display:flex;gap:6px}
.dots i{width:11px;height:11px;border-radius:50%;background:#3a3a3a;display:block}
.dots i.on{background:var(--blue)}

/* services */
.service{top:445px;width:207px}
.service-img{height:94px}
.service-label{margin-top:12px;font-size:11px;color:#333;display:flex;align-items:center;gap:5px;white-space:nowrap}
.tri{width:0;height:0;border-top:4px solid transparent;border-bottom:4px solid transparent;border-left:7px solid var(--blue)}

/* about */
.h2{font-size:19.5px;font-weight:400;color:var(--blue);letter-spacing:.2px}
.about p{font-size:10.9px;line-height:15.4px;color:#444;width:528px}
.about p+p{margin-top:10px}
.read-more{left:490px;top:841px;font-size:10.5px;color:var(--blue);display:flex;align-items:center;gap:5px}

/* lead form */
.offer-bar{left:677px;top:593px;width:195px;height:41px;background:linear-gradient(180deg,var(--orange-light),var(--orange));border-radius:2px;padding:9px 0 0 28px;font-size:12px;font-weight:700;color:#2a1a0a;line-height:13px}
.free-badge{left:603px;top:575px;width:80px;height:80px;border-radius:50%;background:radial-gradient(circle at 40% 35%,#3d95e8,var(--blue-dark));border:3px solid #fff;box-shadow:0 2px 4px rgba(0,0,0,.3);display:flex;align-items:center;justify-content:center;color:#fff;font-size:26px;font-style:italic;font-family:Georgia,serif}
.field{left:620px;width:250px;height:28px;border:1px solid #bbb;border-radius:2px;box-shadow:inset 0 1px 2px rgba(0,0,0,.12);font-size:10px;color:#777;padding:8px 0 0 11px}
.enquire{left:622px;top:830px;width:136px;height:31px;background:linear-gradient(180deg,#2f8ae6,var(--blue-dark));border-radius:2px;color:#fff;font-size:12.5px;font-weight:700;display:flex;align-items:center;justify-content:center}

/* testimonials */
.quote{top:916px;width:230px}
.quote-mark{position:absolute;left:-24px;top:-6px;font-size:30px;color:#c4c4c4;font-family:Georgia,serif;font-weight:700}
.quote p{font-size:10.9px;line-height:15.4px;color:#444}
.quote .who{margin-top:6px;font-size:11.5px;color:#222}
.quote .url{font-size:10.5px;color:var(--blue)}

/* footer */
.footer{left:0;top:1053px;width:916px;height:147px;background:var(--footer)}
.quick-title{left:29px;top:1064px;font-size:15px;color:#fff}
.links{list-style:none;width:154px}
.links li{border-top:1px solid var(--footer-line);font-size:10.2px;color:var(--footer-text);height:20.6px;padding-top:4px}
.links li:last-child{border-bottom:1px solid var(--footer-line)}
.call{right:31px;top:1083px;font-size:12px;color:#ddd;display:flex;align-items:baseline;gap:8px}
.call strong{font-size:19px;font-weight:400;color:#fff}
.follow{right:31px;top:1117px;font-size:12px;color:#ddd;display:flex;align-items:center;gap:9px}
.social{width:28px;height:28px;border-radius:50%;background:#6d7f94;display:block}
.copy{right:31px;top:1160px;font-size:9.6px;color:#ddd}
</style>
</head>
<body>

<header>
  <div class="abs brand"><span class="brand-dot"></span><span class="brand-name">Bright Path Web Growth</span></div>
  <ul class="abs nav">
    <li class="active">HOME</li><li>SERVICES</li><li>ABOUT US</li><li>BLOG</li><li>CONTACT US</li>
  </ul>
</header>

<section class="abs hero">
  <div class="hero-photo" role="img" aria-label="Three business people in suits smiling behind an open laptop"></div>
  <h1 class="tagline">
    <span>We are not about</span> <b>advertising</b><br>
    <span>We are about</span> <b>connecting</b><br>
    <span>your</span> <b>customers,</b> <span>and</span> <b>growing</b><br>
    <span>your</span> <b>business</b>
  </h1>
  <div class="dots"><i></i><i></i><i class="on"></i></div>
</section>

<section class="services">
  <div class="abs service" style="left:28px">
    <div class="service-img" role="img" aria-label="Team planning strategy at a whiteboard" style="background:linear-gradient(135deg,#dfe6ec,#b6c4d2)"></div>
    <div class="service-label">CONSULTING &amp; STRATEGY PLANNING <span class="tri"></span></div>
  </div>
  <div class="abs service" style="left:245px">
    <div class="service-img" role="img" aria-label="Puzzle pieces with search optimisation terms" style="background:linear-gradient(135deg,#e8eaec,#2f7ad8 55%,#e6e8ea)"></div>
    <div class="service-label">SEARCH ENGINE OPTIMISATION <span class="tri"></span></div>
  </div>
  <div class="abs service" style="left:462px">
    <div class="service-img" role="img" aria-label="Hand on a computer mouse with banknotes beside a keyboard" style="background:linear-gradient(135deg,#eef0f1,#cfd5d6 60%,#d9c7b8)"></div>
    <div class="service-label">PAY PER CLICK <span class="tri"></span></div>
  </div>
  <div class="abs service" style="left:678px">
    <div class="service-img" role="img" aria-label="Target with a dart in the centre" style="background:linear-gradient(90deg,#d9d9d9,#f0f0f0)"></div>
    <div class="service-label">RE-MARKETING <span class="tri"></span></div>
  </div>
</section>

<section class="about">
  <h2 class="abs h2" style="left:43px;top:592px">ABOUT BRIGHT PATH</h2>
  <div class="abs" style="left:40px;top:622px">
    <p>Lorem Ipsum is simply dummy text of the printing and typesetting industry. Lorem Ipsum has been the industry's standard dummy text ever since the 1500s, when an unknown printer took a galley of type and scrambled it to make a type specimen book. It has survived not only five centuries, but also the leap into electronic typesetting, remaining essentially unchanged. It was popularised in the 1960s with the release of Letterpane sheets containing Lorem Ipsum passages, and more recently with desktop publishing software like Quillset PageForge including versions of Lorem Ipsum.</p>
    <p>Lorem Ipsum is simply dummy text of the printing and typesetting industry. Lorem Ipsum has been the industry's standard dummy text ever since the 1500s, when an unknown printer took a galley of type and scrambled it to make a type specimen book. It has survived not only five centuries, but also the leap into electronic typesetting, remaining essentially unchanged. It was popularised in the 1960s with the release of Letterpane sheets containing Lorem Ipsum passages, and more recently with desktop publishing software like Quillset PageForge including versions of Lorem Ipsum.</p>
  </div>
  <div class="abs read-more"><span class="tri"></span>READ MORE</div>
</section>

<aside class="lead-form">
  <div class="abs offer-bar">CONSULTATION &amp;<br>WEBSITE AUDIT</div>
  <div class="abs free-badge">free</div>
  <div class="abs field" style="top:663px">NAME *</div>
  <div class="abs field" style="top:704px">EMAIL *</div>
  <div class="abs field" style="top:746px">PHONE *</div>
  <div class="abs field" style="top:787px">WEBSITE</div>
  <div class="abs enquire">ENQUIRE NOW</div>
</aside>

<section class="testimonials">
  <h2 class="abs h2" style="left:43px;top:883px">WHAT PEOPLE SAY :</h2>
  <div class="abs quote" style="left:67px">
    <span class="quote-mark">&ldquo;</span>
    <p>Lorem Ipsum is simply dummy text of the printing and typesetting industry. Lorem Ipsum has been the industry's standard dummy text ever since the 1500s, when an unknown printer......</p>
    <div class="who">Dan Whitcombe</div>
    <div class="url">http://www.brightpathwebgrowth.com.au/</div>
  </div>
  <div class="abs quote" style="left:360px">
    <span class="quote-mark">&ldquo;</span>
    <p>Lorem Ipsum is simply dummy text of the printing and typesetting industry. Lorem Ipsum has been the industry's standard dummy text ever since the 1500s, when an unknown printer......</p>
    <div class="who">Dan Whitcombe</div>
    <div class="url">http://www.brightpathwebgrowth.com.au/</div>
  </div>
  <div class="abs quote" style="left:658px">
    <span class="quote-mark">&ldquo;</span>
    <p>Lorem Ipsum is simply dummy text of the printing and typesetting industry. Lorem Ipsum has been the industry's standard dummy text ever since the 1500s, when an unknown printer......</p>
    <div class="who">Dan Whitcombe</div>
    <div class="url">http://www.brightpathwebgrowth.com.au/</div>
  </div>
</section>

<footer>
  <div class="abs footer"></div>
  <div class="abs quick-title">Quick Links</div>
  <ul class="abs links" style="left:47px;top:1087px">
    <li>About us</li><li>Office Locations</li><li>Programs</li><li>Blog</li>
  </ul>
  <ul class="abs links" style="left:230px;top:1087px">
    <li>About us</li><li>Office Locations</li><li>Programs</li><li>Contact us</li>
  </ul>
  <div class="abs call">CALL US : <strong>(02) 5550 1427</strong></div>
  <div class="abs follow">FOLLOW US :
    <span class="social" role="img" aria-label="Social profile link"></span>
    <span class="social" role="img" aria-label="Social profile link"></span>
    <span class="social" role="img" aria-label="News feed link"></span>
  </div>
  <div class="abs copy">All rights reserved. Bright Path Web Growth, Copyright &copy; 2012</div>
</footer>

</body>
</html>
```